Kestrel Photography Business Card

I need a business card designed for a photography business based in Perth, Western Australia called Kestrel Photography.

We specialise in wedding, event photography and portrait photography.

The business card must borrow the style of the attached logo.

The hex codes for the colours in the logo are:
#ED1D85 - Pink
#89C23E - Green
#37282F - Black

The name on the card will be:
Name: Toviran
Phone: 0417395268
Website: www.kestrelphotography.com.au
Facebook: kestrelphotography

I am open and happy to accept creative concepts.

I’d like some space at the back for writing notes and appointment details.

```html
<!DOCTYPE html>
<html lang="en">
<head>
<meta charset="utf-8">
<title>Kestrel Photography – Business Card</title>
<link rel="stylesheet" href="https://fonts.googleapis.com/css2?family=Montserrat:wght@300;400;500&family=Pinyon+Script&display=swap">
<style>
  :root {
    --pink: #ED1D85;
    --green: #89C23E;
    --green-bright: #5FE01A;
    --green-deep: #1F8A12;
    --black: #37282F;
    --cyan: #3DE3E8;
    --blue: #1F2FD6;
    --white: #FFFFFF;
    --backdrop: #EDEBE6;
    --card-w: 860px;
    --card-h: 531px;
  }
  * { box-sizing: border-box; margin: 0; padding: 0; }
  html, body { width: 1200px; height: 1200px; overflow: hidden; }
  body {
    background: var(--backdrop);
    font-family: "Montserrat", sans-serif;
    position: relative;
  }
  .card {
    position: absolute;
    left: 170px;
    width: var(--card-w);
    height: var(--card-h);
    border-radius: 18px;
    overflow: hidden;
    background: radial-gradient(ellipse 60% 65% at 55% 48%, var(--green-bright) 0%, #3CB51A 55%, var(--green-deep) 100%);
    box-shadow: 0 6px 18px rgba(0,0,0,0.18);
  }
  .card--front { top: 50px; }
  .card--back {
    top: 619px;
    background: linear-gradient(135deg, #4CC21F 0%, #2FA513 100%);
  }

  /* Front */
  .foliage-ornament {
    position: absolute;
    left: 0; top: 0;
    width: 250px; height: 100%;
    background: radial-gradient(ellipse 70% 55% at 20% 55%, rgba(55,40,47,0.85) 0%, rgba(55,40,47,0.55) 55%, rgba(55,40,47,0) 100%);
  }
  .brand-title {
    position: absolute;
    left: 78px; top: 212px;
    width: 720px;
    font-weight: 400;
    font-size: 34px;
    letter-spacing: 13.5px;
    color: var(--black);
    text-transform: uppercase;
    border-bottom: 2px solid var(--black);
    padding-bottom: 4px;
    white-space: nowrap;
  }
  .brand-tagline {
    position: absolute;
    left: 84px; top: 262px;
    width: 720px;
    font-family: "Pinyon Script", cursive;
    font-size: 31px;
    letter-spacing: 4px;
    color: var(--white);
    text-shadow: 0 0 1px var(--black), 1px 1px 0 var(--black);
    white-space: nowrap;
  }

  /* Back */
  .brand-mark {
    position: absolute;
    left: 60px; top: 70px;
    display: flex; align-items: center; gap: 12px;
  }
  .brand-mark__dot {
    width: 34px; height: 34px; border-radius: 50%;
    background: var(--pink);
  }
  .brand-mark__name {
    font-weight: 500;
    font-size: 18px;
    letter-spacing: 1px;
    color: var(--black);
  }
  .person-name {
    position: absolute;
    left: 60px; top: 210px;
    font-weight: 400;
    font-size: 46px;
    letter-spacing: 2px;
    color: var(--black);
    text-transform: uppercase;
    border-bottom: 2px solid var(--black);
    padding-bottom: 2px;
  }
  .notes-panel {
    position: absolute;
    right: 44px; top: 44px;
    width: 380px; height: 250px;
    background: var(--white);
    border-radius: 22px;
    padding: 50px 30px 0;
  }
  .notes-panel__line {
    height: 1.5px;
    background: var(--black);
    margin-bottom: 56px;
  }
  .contact-list {
    position: absolute;
    left: 60px; top: 330px;
    list-style: none;
  }
  .contact-item {
    display: flex; align-items: center; gap: 20px;
    margin-bottom: 22px;
  }
  .contact-item__icon {
    width: 40px; height: 40px;
    display: flex; align-items: center; justify-content: center;
    border-radius: 6px;
  }
  .contact-item__icon--phone { background: var(--pink); }
  .contact-item__icon--web { background: var(--cyan); border-radius: 50%; }
  .contact-item__icon--social { background: var(--blue); }
  .contact-item__value {
    height: 40px;
    padding: 0 18px;
    display: flex; align-items: center;
    color: var(--white);
    font-size: 18px;
    letter-spacing: 5px;
  }
  .contact-item__value--phone { background: var(--pink); letter-spacing: 8px; }
  .contact-item__value--web { background: var(--cyan); color: #1C6B70; font-size: 15px; letter-spacing: 1px; }
  .contact-item__value--social { background: var(--blue); letter-spacing: 1.5px; }
</style>
</head>
<body>
  <section class="card card--front" aria-label="Business card front">
    <div class="foliage-ornament" role="img" aria-label="Dark leafy foliage ornament"></div>
    <h1 class="brand-title">Kestrel Photography</h1>
    <p class="brand-tagline">Wedding, Event And Portrait Photography</p>
  </section>

  <section class="card card--back" aria-label="Business card back">
    <div class="brand-mark">
      <span class="brand-mark__dot"></span>
      <span class="brand-mark__name">Kestrel Photography</span>
    </div>
    <h2 class="person-name">Toviran</h2>
    <div class="notes-panel" aria-label="Space for notes and appointments">
      <div class="notes-panel__line"></div>
      <div class="notes-panel__line"></div>
      <div class="notes-panel__line"></div>
    </div>
    <ul class="contact-list">
      <li class="contact-item">
        <span class="contact-item__icon contact-item__icon--phone">
          <svg width="24" height="24" viewBox="0 0 24 24" aria-hidden="true"><path fill="#FFFFFF" d="M6.6 10.8c1.4 2.8 3.8 5.1 6.6 6.6l2.2-2.2c.3-.3.7-.4 1-.2 1.1.4 2.3.6 3.6.6.6 0 1 .4 1 1V20c0 .6-.4 1-1 1C10.6 21 3 13.4 3 4c0-.6.4-1 1-1h3.5c.6 0 1 .4 1 1 0 1.3.2 2.5.6 3.6.1.3 0 .7-.2 1z"/></svg>
        </span>
        <span class="contact-item__value contact-item__value--phone">0417395268</span>
      </li>
      <li class="contact-item">
        <span class="contact-item__icon contact-item__icon--web">
          <svg width="26" height="26" viewBox="0 0 24 24" aria-hidden="true"><g fill="none" stroke="#1C6B70" stroke-width="1.6"><circle cx="12" cy="12" r="9"/><ellipse cx="12" cy="12" rx="4" ry="9"/><path d="M3 12h18"/></g></svg>
        </span>
        <span class="contact-item__value contact-item__value--web">www.kestrelphotography.com.au</span>
      </li>
      <li class="contact-item">
        <span class="contact-item__icon contact-item__icon--social"></span>
        <span class="contact-item__value contact-item__value--social">kestrelphotography</span>
      </li>
    </ul>
  </section>
</body>
</html>
```